I need business cards for a company that will be an umbrella for many retail stores. I need them to be sleek and modern. I would like some white and black in the background of the card as these are the office colours the logo is attached.
Target Market(s)
worldwide
Industry/Entity Type
Business
Requirements
Must have
- traditional business card shape
Should not have
- too many colours
no swirly text

```html
<!DOCTYPE html>
<html lang="en">
<head>
<meta charset="utf-8">
<title>Norvale General Trading – Business Card</title>
<link href="https://fonts.googleapis.com/css2?family=Cinzel:wght@400;500&family=Arimo:wght@400&display=swap" rel="stylesheet">
<style>
  :root {
    --backdrop: #d6d6d8;
    --card-dark: #02060b;
    --card-glow: #0f4686;
    --card-light: #ffffff;
    --ink: #1e1e1e;
    --ink-soft: #555a60;
    --accent: #1a6fb8;
    --mark-light: #dfe6f0;
    --mark-dark: #3a5d8a;
    --label: #3a3a3a;
  }
  * { margin: 0; padding: 0; box-sizing: border-box; }
  html, body { width: 1200px; height: 895px; overflow: hidden; }
  body { background: var(--backdrop); position: relative; font-family: "Arimo", Arial, sans-serif; }

  .card {
    position: absolute;
    top: 302px;
    width: 569px;
    height: 342px;
    border-radius: 14px;
    overflow: hidden;
  }

  /* Front */
  .card--front { left: 18px; background: var(--card-dark); }
  .card--front .texture {
    position: absolute; inset: 0;
    background:
      radial-gradient(ellipse 38% 55% at 45% 38%, rgba(25, 95, 175, 0.55), transparent 72%),
      radial-gradient(ellipse 30% 30% at 45% 80%, rgba(15, 60, 115, 0.35), transparent 75%),
      linear-gradient(180deg, #071629 0%, var(--card-dark) 100%);
  }
  .card--front .divider {
    position: absolute; left: 0; right: 0; top: 221px; height: 14px;
    background: linear-gradient(180deg, rgba(0,0,0,0.75), transparent);
  }
  .card--front .brand {
    position: absolute; left: 178px; top: 138px;
    display: flex; align-items: center; gap: 10px;
    color: var(--mark-light);
  }

  /* Back */
  .card--back { left: 613px; background: var(--card-light); }
  .card--back .texture {
    position: absolute; left: 176px; top: 40px; width: 256px; height: 240px;
    background:
      radial-gradient(ellipse 50% 50% at 50% 50%, rgba(190, 196, 206, 0.35), rgba(220, 224, 230, 0.15) 60%, transparent 100%);
  }
  .card--back .divider {
    position: absolute; left: 0; right: 0; top: 220px; height: 10px;
    background: linear-gradient(180deg, #cfd1d4 0, #f3f3f3 40%, transparent);
  }
  .contact { position: absolute; left: 83px; top: 88px; }
  .contact__name {
    font-family: "Cinzel", Georgia, serif; font-weight: 500;
    font-size: 17px; color: var(--ink); letter-spacing: 0.3px;
  }
  .contact__company { font-size: 11px; color: var(--ink-soft); margin: 1px 0 6px 2px; }
  .contact__line {
    display: flex; align-items: center; gap: 6px;
    font-size: 11.5px; color: var(--ink-soft); height: 16px;
  }
  .contact__line svg { width: 14px; height: 12px; fill: var(--accent); }
  .contact__address { padding-left: 20px; margin-top: 3px; }
  .contact__web {
    font-size: 8px; color: var(--accent); letter-spacing: 11.5px;
    margin-top: 6px; white-space: nowrap;
  }
  .card--back .brand {
    position: absolute; left: 380px; top: 250px;
    display: flex; align-items: center; gap: 8px;
    color: var(--mark-dark);
  }

  .brand__dot { width: 30px; height: 30px; border-radius: 50%; background: currentColor; }
  .brand__name { font-family: "Cinzel", Georgia, serif; font-weight: 400; line-height: 1.05; }
  .card--front .brand__name { font-size: 17px; }
  .card--back .brand__name { font-size: 13px; }
  .brand__name span { display: block; }

  .side-label {
    position: absolute; top: 684px;
    font-family: "Cinzel", Georgia, serif; font-size: 14px;
    letter-spacing: 3.5px; color: var(--label);
  }
  .side-label--front { left: 66px; }
  .side-label--back { left: 660px; }
</style>
</head>
<body>
  <section class="card card--front" aria-label="Card front">
    <div class="texture" role="img" aria-label="Dark blue decorative streak texture"></div>
    <div class="brand">
      <div class="brand__dot"></div>
      <div class="brand__name"><span>Norvale</span><span>General Trading</span></div>
    </div>
    <div class="divider"></div>
  </section>

  <section class="card card--back" aria-label="Card back">
    <div class="texture" role="img" aria-label="Faint grey decorative streak texture"></div>
    <div class="contact">
      <div class="contact__name">Your Name here</div>
      <div class="contact__company">company name</div>
      <div class="contact__line">
        <svg viewBox="0 0 14 12"><path d="M1 4c2-3 10-3 12 0v1.5h-3V4H4v1.5H1z"/><rect x="2" y="6" width="10" height="6" rx="1"/></svg>
        123.4567.890
      </div>
      <div class="contact__line">
        <svg viewBox="0 0 14 12"><rect x="3" y="0" width="8" height="4"/><rect x="0" y="5" width="14" height="7" rx="1"/></svg>
        123.4567.890
      </div>
      <div class="contact__line">
        <svg viewBox="0 0 14 12"><rect x="0" y="1" width="14" height="10" rx="1"/><path d="M0.5 1.5L7 7l6.5-5.5" stroke="#fff" stroke-width="1.3" fill="none"/></svg>
        your email address here
      </div>
      <div class="contact__line contact__address">address here</div>
      <div class="contact__web">your website here</div>
    </div>
    <div class="divider"></div>
    <div class="brand">
      <div class="brand__dot"></div>
      <div class="brand__name"><span>Norvale</span><span>General Trading</span></div>
    </div>
  </section>

  <div class="side-label side-label--front">FRONT</div>
  <div class="side-label side-label--back">BACK</div>
</body>
</html>
```